Lantern Ridge Treks Flyer

I have an adventure travel company and I need a flyer to promote my trip to Ukraine.
I would like to have a universal flyer that I can change based on the trip.
The Title should say "Travel to Ukraine: 9 Day Eastern European Adventure"
The date should be under the title.
The background photo should be kiev2.jpg
The highlights of the trip, then price $1200 and what it includes. See the text for highlights and includes sections here:
http://www.lanternridgetreks.com/#!featured-trip
The website link (www.lanternridgetreks.com) should be somewhere in the bottom.
You can use other photos provided or from my website that relates to Ukraine trip.
Travel

```html
<!DOCTYPE html>
<html lang="en">
<head>
<meta charset="utf-8">
<title>Travel to Ukraine – 9 Day Eastern European Adventure</title>
<link rel="stylesheet" href="https://fonts.googleapis.com/css2?family=Tinos:wght@700&family=Arimo:wght@700&display=swap">
<style>
  :root {
    --paper: #ffffff;
    --ink: #111111;
    --date-ink: #3a3a3a;
    --sky: #dfe4e8;
    --city: #b9bfb6;
    --river: #a9b7c0;
    --trees: #96a68a;
    --gold: #dcc57c;
    --roof: #c6c7c1;
    --veil: rgba(255, 255, 255, 0.3);
  }
  * { margin: 0; padding: 0; box-sizing: border-box; }
  html, body {
    width: 1200px;
    height: 927px;
    overflow: hidden;
    background: var(--paper);
  }
  .flyer {
    position: relative;
    width: 1200px;
    height: 927px;
    background: var(--paper);
  }
  .hero-photo {
    position: absolute;
    left: 41px;
    top: 59px;
    width: 1121px;
    height: 819px;
    background:
      radial-gradient(ellipse 26% 42% at 60% 58%, var(--gold) 0%, rgba(220, 197, 124, 0.55) 45%, rgba(220, 197, 124, 0) 80%),
      radial-gradient(ellipse 10% 18% at 84% 60%, rgba(220, 197, 124, 0.8) 0%, rgba(220, 197, 124, 0) 100%),
      radial-gradient(ellipse 10% 18% at 36% 56%, rgba(220, 197, 124, 0.7) 0%, rgba(220, 197, 124, 0) 100%),
      linear-gradient(180deg,
        var(--sky) 0%,
        var(--sky) 9%,
        var(--city) 16%,
        var(--trees) 22%,
        var(--river) 28%,
        var(--river) 36%,
        var(--trees) 42%,
        var(--trees) 55%,
        var(--roof) 66%,
        var(--roof) 100%);
  }
  .hero-photo::after {
    content: "";
    position: absolute;
    inset: 0;
    background: var(--veil);
  }
  .title {
    position: absolute;
    font-family: "Tinos", "Times New Roman", serif;
    font-weight: 700;
    font-size: 64px;
    line-height: 1;
    color: var(--ink);
    transform: scaleX(0.86);
    transform-origin: left center;
    white-space: nowrap;
  }
  .title-line-1 { left: 74px; top: 73px; }
  .title-line-2 { left: 299px; top: 147px; }
  .trip-meta {
    position: absolute;
    top: 229px;
    font-family: "Arimo", Arial, sans-serif;
    font-weight: 700;
    font-size: 67px;
    line-height: 1;
    letter-spacing: 2px;
    color: var(--date-ink);
    text-shadow: 2px 2px 3px rgba(0, 0, 0, 0.35);
    transform: scaleX(1.14);
    transform-origin: left center;
    white-space: nowrap;
  }
  .trip-dates { left: 100px; }
  .trip-price { left: 862px; }
  .trip-copy {
    position: absolute;
    left: 69px;
    top: 516px;
    width: 1090px;
    font-family: "Tinos", "Times New Roman", serif;
    font-weight: 700;
    font-size: 29px;
    line-height: 36.5px;
    color: var(--ink);
  }
  .trip-copy p { margin-bottom: 46px; white-space: nowrap; }
  .trip-copy p:last-child { margin-bottom: 0; }
  .indent { padding-left: 6px; }
</style>
</head>
<body>
  <main class="flyer">
    <div class="hero-photo" role="img" aria-label="Aerial view of Kyiv with golden church domes, green trees and the wide river behind"></div>

    <h1>
      <span class="title title-line-1">"Travel to Ukraine:</span>
      <span class="title title-line-2">9 Day Eastern European Adventure"</span>
    </h1>

    <div class="trip-meta trip-dates">May 18 -May 27</div>
    <div class="trip-meta trip-price">$1,200</div>

    <section class="trip-copy">
      <p>Authentic travel experience that will leave you an outlook on the history and culture<br><span class="indent">as well as the natural beauty.</span></p>
      <p>You will experience urban "must-see" sights with the outdoor<br>adventures in the countryside offering the most spectacular scenery.<br>Highly trusted and experienced local guides in every place we visit, high-quality<br>accommodations and great food will make your trip a safe and pleasant vacation.</p>
      <p>We are looking forward to experiencing new adventures with you on our next trip.</p>
    </section>
  </main>
</body>
</html>
```